RLT Gourmet Mushrooms web presence and site

The goal is to attract local buyers of fresh mushrooms and to both local and international buyers freeze dried mushrooms. Mushrooms grown will be oyster mushrooms (yellow, pink, blue, king), shiitake, lions main, chestnut, and more. My business will also be selling grow kits that help families who would like to grow there own mushrooms

Target Market(s)

Local restaurants, foodies and people seeking high quality fresh and freeze dried gourmet mushrooms

Coding

Number of Pages Required

1 page

Font styles to use
Serif

Requirements
Must have
• Pictures of the various mushrooms grown along with the characteristics of each of the mushrooms. Recipes and cooking tips for the various mushrooms. There needs to be
1. Order forms with online payments
2. Feedback
3. Preorders for mushrooms that may be more seasonal
4.links to social media Facebook, LinkedIn, etc... I am not knowledgeable in this area
5. Contact Us link email, address, phone
6. About Us link explaining Peter Vonk & Marla Densworth and a brief explanation about us and why we became Mushroom farmers
7. Descriptions of the various mushroom varieties grown and how they are best prepared and served
8. Why Freeze Drying mushrooms and the benefits of Freeze Drying over other methods of preservation.
Nice to have
• 1. Recipes and cooking tips for each of the mushrooms.
2. Weekly additional resources added to different pages
3. Q&A section
4. Food Blog with resources added weekly
5.

Flexibility with future expansion and growth is essential. I would like to have a growing site, not a stagnant site.
Should not have
• 1. Boring, bland presentation.
2. The web site is one to educate, promote the various mushrooms grown
3. No music, video or sound on the main pages but eventually a Vlog might be in the works.

I realize there is a lot of content requested but the content needs to attract buyers and to have the site a go to site for foodies

```html
<!DOCTYPE html>
<html lang="en">
<head>
<meta charset="utf-8">
<title>RLT Gourmet Mushrooms</title>
<link href="https://fonts.googleapis.com/css2?family=Poppins:wght@300;400;500;600&display=swap" rel="stylesheet">
<style>
:root{
  --green:#6cb614;
  --green-light:#cbe5ad;
  --navy:#262b45;
  --ink:#2d2f3f;
  --muted:#6b6d7a;
  --page:#f5f6f9;
  --footer:#1f2138;
  --star:#f2a01c;
  --link:#3b3f8f;
}
*{margin:0;padding:0;box-sizing:border-box}
html,body{width:1200px;height:3034px;overflow:hidden}
body{font-family:"Poppins",sans-serif;color:var(--ink);background:var(--page);position:relative}

.topbar{height:57px;background:#fff;position:relative}
.topbar .contact{position:absolute;left:230px;top:21px;font-size:11px;color:var(--muted);display:flex;gap:16px;align-items:center}
.topbar .contact svg{margin-right:5px;vertical-align:-2px}
.brand{position:absolute;left:0;right:0;top:17px;text-align:center;font-size:18px;font-weight:500;line-height:23px;color:var(--navy)}
.topbar .tools{position:absolute;right:228px;top:19px;display:flex;gap:10px;align-items:center}
.dot-icon{width:12px;height:12px;border-radius:50%;background:var(--navy)}
.sep{width:1px;height:16px;background:#ccc}

.nav{height:41px;background:var(--green);display:flex;align-items:center;padding-left:235px;gap:31px}
.nav a{color:#fff;text-decoration:none;font-size:12.5px;font-weight:500}

.hero{height:433px;position:relative;background:radial-gradient(ellipse at 60% 35%,#7a4a2e 0,#5a3a22 22%,#3f5a24 45%,#2c4a1a 75%,#1f3512 100%);display:flex;flex-direction:column;align-items:center}
.hero h1{margin-top:108px;color:#fff;font-size:48px;font-weight:500;line-height:57px;text-align:center}
.btn{display:inline-block;background:var(--green);color:#fff;font-size:13px;font-weight:500;border-radius:20px;text-align:center}
.hero .btn{margin-top:28px;width:148px;height:36px;line-height:36px}
.dots{position:absolute;top:380px;left:0;right:0;display:flex;justify-content:center;gap:8px}
.dots i{width:7px;height:7px;border:1px solid #fff;border-radius:50%}
.dots i.on{background:#fff}
.tear{height:105px;background:linear-gradient(#e4e4e4,#f1f1f2 60%,var(--page))}

.products{display:grid;grid-template-columns:repeat(3,210px);gap:27px 27px;justify-content:center;margin-top:25px}
.card{background:#fff;height:278px}
.card .photo{height:164px}
.card h3{font-size:13px;font-weight:500;margin:14px 18px 0}
.card p{font-size:11px;color:var(--muted);line-height:16px;margin:3px 18px 0;font-weight:300}
.card .foot{display:flex;justify-content:space-between;margin:12px 18px 0;font-size:10.5px;font-weight:600}
.stars{color:var(--star);font-size:10px;letter-spacing:1px}
.browse{display:block;width:189px;height:36px;line-height:36px;margin:39px auto 0;box-shadow:0 6px 12px rgba(108,182,20,.3)}

.banner{height:178px;position:relative}
.banner-fresh{margin-top:71px;background:radial-gradient(ellipse at 58% 30%,#bdb3a5 0,#7a6a58 15%,#3a2e24 40%,#241c16 100%)}
.banner-recipes{background:radial-gradient(ellipse at 38% 100%,#c8b8aa 0,#6c7a4a 22%,#2f5418 55%,#1c3010 100%)}
.banner .lines{position:absolute;color:#fff;font-size:25px;line-height:38px}
.banner .btn{position:absolute;width:130px;height:35px;line-height:35px}

.feedback{height:374px;text-align:center;position:relative}
.feedback h2{padding-top:64px;font-size:25px;font-weight:600;color:var(--navy)}
.sub{font-size:11px;color:var(--ink);margin-top:4px}
.avatars{display:flex;justify-content:center;align-items:center;gap:12px;margin-top:36px}
.avatars i{width:56px;height:56px;border-radius:50%;background:var(--green-light)}
.avatars i.on{width:69px;height:69px;background:var(--green)}
.quote{font-size:12.5px;line-height:21px;margin-top:30px;font-weight:300}
.author{color:var(--green);font-size:12.5px;margin-top:14px}

.blog{height:575px;text-align:center}
.blog .kicker{padding-top:57px;font-size:11px}
.blog h2{font-size:25px;font-weight:300;margin-top:6px}
.blog h2 b{color:var(--green);font-weight:600}
.posts{display:grid;grid-template-columns:repeat(3,234px);gap:19px;justify-content:center;margin-top:38px;text-align:left}
.post .photo{height:189px;position:relative;border-radius:3px}
.date{position:absolute;left:10px;top:8px;width:38px;height:38px;border-radius:50%;background:#fff;font-size:8px;line-height:9px;text-align:center;padding-top:10px;font-weight:500}
.meta{font-size:9px;color:var(--link);margin-top:26px;display:flex;gap:12px}
.post h3{font-size:13.5px;font-weight:500;line-height:20px;margin-top:7px}
.post p{font-size:10px;color:var(--muted);line-height:19px;margin-top:7px}
.post .more{font-size:10px;color:var(--link);margin-top:8px;display:block}

.footer{height:339px;background:var(--footer);color:#fff;position:relative}
.footer .col{position:absolute;top:60px}
.footer .logo{font-size:19px;font-weight:500;line-height:24px;color:#fff}
.footer .phone{font-size:14px;margin-top:18px}
.footer h4{font-size:11px;font-weight:500}
.footer small{display:block;font-size:9px;color:#a8aabb;line-height:17px}
.footer ul{list-style:none;margin-top:10px}
.footer li{font-size:10px;color:#a8aabb;line-height:20.5px}
.newsletter{display:flex;margin-top:12px;width:268px;height:28px}
.newsletter .field{flex:1;background:#fff;border-radius:14px 0 0 14px;font-size:10px;color:#999;padding:7px 20px}
.newsletter .go{width:90px;background:var(--green);border-radius:0 14px 14px 0;font-size:11px;font-weight:500;text-align:center;line-height:28px}
.social{display:flex;gap:10px;margin-top:10px}
.social i{width:9px;height:9px;border-radius:50%;background:#a8aabb}
.copy{position:absolute;left:0;right:0;top:258px;border-top:1px solid #2d3050;text-align:center;padding-top:34px;font-size:10px;color:#a8aabb}
</style>
</head>
<body>

<header class="topbar">
  <div class="contact">
    <span><svg width="13" height="10" viewBox="0 0 13 10"><rect x=".5" y=".5" width="12" height="9" fill="none" stroke="#6b6d7a"/><path d="M.5 .5 6.5 5.5 12.5 .5" fill="none" stroke="#6b6d7a"/></svg>Email Addrests</span>
    <span>12 3456 789</span>
  </div>
  <div class="brand">RLT Gourmet Mushrooms</div>
  <div class="tools">
    <svg width="14" height="14" viewBox="0 0 14 14"><circle cx="6" cy="6" r="4.5" fill="none" stroke="#262b45" stroke-width="1.4"/><path d="M9.5 9.5 13 13" stroke="#262b45" stroke-width="1.4"/></svg>
    <span class="sep"></span>
    <i class="dot-icon" aria-label="Social link"></i>
    <i class="dot-icon" aria-label="Social link"></i>
    <i class="dot-icon" aria-label="Social link"></i>
  </div>
</header>

<nav class="nav">
  <a href="#">Home</a><a href="#">Order Forms</a><a href="#">About Us</a><a href="#">Preorders</a><a href="#">Descriptions</a><a href="#">benefits of Freeze</a><a href="#">Blog</a><a href="#">Contact Us</a>
</nav>

<section class="hero" role="img" aria-label="Large brown-capped mushroom growing in green grass">
  <h1>RLT Gourmet<br>Mushrooms</h1>
  <span class="btn">Order Now</span>
  <div class="dots"><i></i><i class="on"></i><i></i></div>
</section>
<div class="tear"></div>

<section class="products">
  <article class="card"><div class="photo" role="img" aria-label="Cluster of yellow mushrooms in grass" style="background:linear-gradient(135deg,#3d4a1c,#c89a2a 55%,#5a5a20)"></div><h3>Yellow Mushrooms</h3><p>Lorem Ipsum is simply<br>dummy text of the printing</p><div class="foot"><span>Order Now</span><span class="stars">★★★★☆</span></div></article>
  <article class="card"><div class="photo" role="img" aria-label="Pink oyster mushrooms on wooden board" style="background:linear-gradient(135deg,#8a6a5a,#e07a5e 50%,#7a6050)"></div><h3>Pink Mushrooms</h3><p>Lorem Ipsum is simply<br>dummy text of the printing</p><div class="foot"><span>Order Now</span><span class="stars">★★★★☆</span></div></article>
  <article class="card"><div class="photo" role="img" aria-label="Blue mushroom in moss" style="background:radial-gradient(circle at 45% 35%,#2a5ad0,#3a5a20 45%,#7a8a30)"></div><h3>Blue Mushrooms</h3><p>Lorem Ipsum is simply<br>dummy text of the printing</p><div class="foot"><span>Order Now</span><span class="stars">★★★★☆</span></div></article>
  <article class="card"><div class="photo" role="img" aria-label="White king mushrooms on grass" style="background:linear-gradient(135deg,#4a7a2a,#ddd4c4 55%,#5a8a30)"></div><h3>King Mushrooms</h3><p>Lorem Ipsum is simply<br>dummy text of the printing</p><div class="foot"><span>Order Now</span><span class="stars">★★★★☆</span></div></article>
  <article class="card"><div class="photo" role="img" aria-label="Pile of shiitake mushrooms" style="background:linear-gradient(135deg,#4a3a2c,#8a6e56 50%,#3a2e24)"></div><h3>Shiitake Mushrooms</h3><p>Lorem Ipsum is simply<br>dummy text of the printing</p><div class="foot"><span>Order Now</span><span class="stars">★★★★☆</span></div></article>
  <article class="card"><div class="photo" role="img" aria-label="Lion's mane mushrooms on pale background" style="background:radial-gradient(circle at 50% 55%,#e8d2a4,#eef4e2 65%)"></div><h3>Lions Main Mushrooms</h3><p>Lorem Ipsum is simply<br>dummy text of the printing</p><div class="foot"><span>Order Now</span><span class="stars">★★★★☆</span></div></article>
</section>
<span class="btn browse">Browse All Mushrooms</span>

<section class="banner banner-fresh" role="img" aria-label="Blurred pale mushroom on dark forest floor">
  <div class="lines" style="left:229px;top:45px">Fresh Mushrooms &amp;<br><span style="padding-left:55px">freeze dried mushrooms</span></div>
  <span class="btn" style="left:840px;top:70px">Order Now</span>
</section>

<section class="feedback">
  <h2>Feedback</h2>
  <p class="sub">Look at our latest Products Lorem Ipsum is simply dummy text of the printing</p>
  <div class="avatars"><i></i><i class="on"></i><i></i></div>
  <p class="quote">This is due to their excellent service, competitive pricing and customer support.<br>It's throughly refresing to get such a personal touch.</p>
  <p class="author">Dana Whitfield</p>
  <svg style="position:absolute;left:205px;top:216px" width="8" height="12" viewBox="0 0 8 12"><path d="M6 1 1 6l5 5" fill="none" stroke="#2d2f3f" stroke-width="1.5"/></svg>
  <svg style="position:absolute;left:970px;top:200px" width="40" height="40" viewBox="0 0 40 40"><circle cx="20" cy="20" r="20" fill="#e6e7ec"/><path d="M18 15l5 5-5 5" fill="none" stroke="#fff" stroke-width="1.5"/></svg>
</section>

<section class="banner banner-recipes" role="img" aria-label="Blurred mushrooms among green foliage">
  <div class="lines" style="left:268px;top:45px;text-align:center">Recipes and cooking<br>Tips for the various mushrooms</div>
  <span class="btn" style="left:845px;top:71px">Click Here</span>
</section>

<section class="blog">
  <p class="kicker">Blog</p>
  <h2>News and &nbsp;<b>Articles</b></h2>
  <p class="sub">Look at our latest Products Lorem Ipsum is simply dummy text of the printing</p>
  <div class="posts">
    <article class="post"><div class="photo" role="img" aria-label="Small orange mushrooms on a dark log" style="background:linear-gradient(135deg,#2a241c,#c8582e 50%,#3a2e22)"><span class="date">30<br>Nov</span></div><div class="meta"><span>By Admin</span><span>.</span><span>2 Comments</span></div><h3>Lorem Ipsum is simply dummy text of the printing</h3><p>There are many variations of passages of available but majority have alteration</p><span class="more">Read More</span></article>
    <article class="post"><div class="photo" role="img" aria-label="Wooden bowl of mixed mushrooms and herbs" style="background:radial-gradient(circle at 50% 50%,#c8a070,#6a4a2c 60%,#8a6a44)"><span class="date">26<br>Nov</span></div><div class="meta"><span>By Admin</span><span>.</span><span>2 Comments</span></div><h3>Lorem Ipsum is simply dummy text of the printing</h3><p>There are many variations of passages of available but majority have alteration</p><span class="more">Read More</span></article>
    <article class="post"><div class="photo" role="img" aria-label="Reddish brown mushrooms against dark background" style="background:radial-gradient(circle at 55% 50%,#9a5050,#4a2a2a 55%,#201818)"><span class="date">20<br>Nov</span></div><div class="meta"><span>By Admin</span><span>.</span><span>2 Comments</span></div><h3>Lorem Ipsum is simply dummy text of the printing</h3><p>There are many variations of passages of available but majority have alteration</p><span class="more">Read More</span></article>
  </div>
</section>

<footer class="footer">
  <div class="col" style="left:230px;top:72px">
    <div class="logo">RLT Gourmet Mushrooms</div>
    <p class="phone">+123 &nbsp;(456-7890)</p>
    <h4 style="margin-top:16px;font-weight:400">Contact</h4>
    <small>Lorem Ipsum is simply dummy text of the printing<br>and typesetting industry.</small>
  </div>
  <div class="col" style="left:524px;top:68px">
    <h4>Quick Links</h4>
    <ul><li>Home</li><li>Order Form</li><li>About Us</li><li>Preorders</li><li>Blog</li><li>Contact Us</li></ul>
  </div>
  <div class="col" style="left:702px;top:68px">
    <h4>WRITE TO US</h4>
    <small style="margin-top:10px">Provide your email below to subscribe to our newsletter</small>
    <div class="newsletter"><span class="field">Email address</span><span class="go">Subscribe</span></div>
    <h4 style="margin-top:14px;font-size:10px">FOLLOW US</h4>
    <div class="social"><i></i><i></i><i></i><i></i><i></i></div>
  </div>
  <div class="copy">Copyright 2020 RLT Gourmet Mushrooms</div>
</footer>

</body>
</html>
```